Gobo Flyer to generate sales and to use at trade shows or as a leave behind to client

We are looking to create a flyer to promote our new exterior or interior event lighting options. We are looking for the layout to be clean and consistent with our color scheme. We are a professional technologically advanced company looking to take your event to the next level. We are looking for a layout which has an image at the top as well as a few other images to allow reader to see a few options

Target Market(s)

Residential as well as commercial

Industry/Entity Type

Trade

Requirements
Must have
• Need the round images to create a collage. and include the text samples of what is available

```html
<!DOCTYPE html>
<html lang="en">
<head>
<meta charset="utf-8">
<title>Projected Illuminations Flyer</title>
<link rel="stylesheet" href="https://fonts.googleapis.com/css2?family=Michroma&family=Montserrat:wght@500;600;700;800&family=Nanum+Pen+Script&display=swap">
<style>
  :root {
    --sky-deep: #0d5fa6;
    --sky-mid: #2a8fd4;
    --sky-light: #4cb3e6;
    --sky-pale: #bfe3f5;
    --paper: #ffffff;
    --ink: #111111;
    --brand-blue: #1f6fc0;
    --band-blue: #2462b0;
    --ring: #5fc1ec;
    --steel: #6d6f73;
  }
  * { margin: 0; padding: 0; box-sizing: border-box; }
  html, body { width: 849px; height: 1200px; overflow: hidden; background: var(--paper); }
  .flyer {
    position: relative; width: 849px; height: 1200px; overflow: hidden;
    font-family: "Montserrat", sans-serif; color: var(--ink);
    background: linear-gradient(180deg, var(--sky-deep) 0%, var(--sky-mid) 22%, var(--sky-light) 52%, #5cbdea 68%, var(--sky-pale) 82%, var(--paper) 90%);
  }
  .headline {
    position: absolute; top: 52px; left: 0; width: 100%; text-align: center;
    font-family: "Michroma", sans-serif; color: #f4f6f8; line-height: 1.06;
    text-shadow: 0 2px 6px rgba(0, 30, 70, .45);
  }
  .headline .line-one { display: block; font-size: 57px; }
  .headline .line-two { display: block; font-size: 57px; letter-spacing: -1px; }
  .collage { position: absolute; top: 0; left: 0; }
  .events-panel {
    position: absolute; left: 56px; top: 553px; width: 248px; height: 385px;
    background: linear-gradient(180deg, #ffffff 0%, #ffffff 55%, rgba(255,255,255,.4) 100%);
  }
  .events-title {
    margin-top: 44px; text-align: center; font-family: "Michroma", sans-serif;
    font-size: 21px; line-height: 1.08; font-weight: 400; letter-spacing: -.5px;
  }
  .events-list { list-style: none; margin: 22px 0 0 58px; font-size: 16px; font-weight: 600; line-height: 1.28; }
  .events-list li { position: relative; margin-bottom: 10px; }
  .events-list li::before { content: "•"; position: absolute; left: -25px; }
  .intro {
    position: absolute; left: 353px; top: 592px; width: 450px;
    font-size: 14.6px; font-weight: 600; line-height: 1.5; color: var(--ink);
  }
  .design-box {
    position: absolute; left: 341px; top: 667px; width: 440px; height: 151px;
    background: var(--paper); border: 1.5px solid #9fb3c2; border-radius: 18px;
  }
  .design-box p {
    margin-top: 13px; text-align: center; font-size: 14.6px; font-weight: 600; line-height: 1.5;
  }
  .gobo-row { position: absolute; left: 0; top: 59px; width: 100%; height: 76px; }
  .gobo-letters {
    position: absolute; left: 99px; top: 3px; width: 70px; height: 70px; border-radius: 50%;
    background: #0c0c0c; color: #fff; font-size: 9.5px; line-height: 1.12; text-align: center;
    padding-top: 9px; font-weight: 500;
  }
  .offer { position: absolute; left: 352px; top: 822px; }
  .offer-lead { font-family: "Nanum Pen Script", cursive; font-size: 40px; line-height: 1; color: #1c1c1c; }
  .offer-price { font-size: 46px; font-weight: 800; color: var(--brand-blue); line-height: 1; margin-top: 2px; }
  .offer-term { font-size: 18.5px; font-weight: 700; color: var(--brand-blue); margin-top: 6px; letter-spacing: .3px; }
  .offer-detail { font-size: 10.5px; font-weight: 600; line-height: 1.3; margin-top: 3px; letter-spacing: .3px; }
  .brand {
    position: absolute; left: 0; top: 1040px; width: 100%;
    display: flex; align-items: center; justify-content: center; gap: 22px;
  }
  .brand-mark { width: 58px; height: 58px; background: var(--brand-blue); }
  .brand-name {
    font-family: "Michroma", sans-serif; font-size: 46px; color: var(--brand-blue);
    letter-spacing: 1px; line-height: 1;
  }
  .contact-band {
    position: absolute; left: 0; bottom: 0; width: 100%; height: 53px; background: var(--band-blue);
    color: #fff; font-size: 16.5px; font-weight: 500; letter-spacing: .5px;
    display: flex; align-items: center; justify-content: center; padding-left: 60px;
  }
  .contact-band .sep { display: inline-block; width: 8px; height: 8px; background: #fff; margin: 0 8px 2px; }
</style>
</head>
<body>
<main class="flyer">
  <h1 class="headline">
    <span class="line-one">PROJECTED</span>
    <span class="line-two">ILLUMINATIONS</span>
  </h1>

  <svg class="collage" width="849" height="1200" viewBox="0 0 849 1200">
    <defs>
      <radialGradient id="night-house-a" cx="50%" cy="45%" r="60%">
        <stop offset="0" stop-color="#8a4c9a"/><stop offset=".55" stop-color="#3a2a4a"/><stop offset="1" stop-color="#3c3126"/>
      </radialGradient>
      <radialGradient id="night-house-hearts" cx="50%" cy="55%" r="60%">
        <stop offset="0" stop-color="#c2309a"/><stop offset=".45" stop-color="#8e1e3a"/><stop offset="1" stop-color="#1c1418"/>
      </radialGradient>
      <radialGradient id="night-house-b" cx="50%" cy="40%" r="60%">
        <stop offset="0" stop-color="#7a5a7a"/><stop offset=".6" stop-color="#2c2a3a"/><stop offset="1" stop-color="#5a4630"/>
      </radialGradient>
      <radialGradient id="night-house-c" cx="45%" cy="40%" r="60%">
        <stop offset="0" stop-color="#b05ab8"/><stop offset=".6" stop-color="#3e2c48"/><stop offset="1" stop-color="#5e4a30"/>
      </radialGradient>
    </defs>
    <circle cx="740" cy="365" r="131" fill="url(#night-house-c)" stroke="var(--ring)" stroke-width="5" role="img" aria-label="Photo of a house lit in purple wall-wash light at night"/>
    <circle cx="112" cy="448" r="117" fill="url(#night-house-a)" stroke="var(--ring)" stroke-width="5" role="img" aria-label="Photo of a house lit with projected patterns and purple light at night"/>
    <circle cx="570" cy="433" r="117" fill="url(#night-house-b)" stroke="var(--ring)" stroke-width="5" role="img" aria-label="Photo of a house with red and white projected lighting at night"/>
    <circle cx="331" cy="385" r="175" fill="url(#night-house-hearts)" stroke="var(--ring)" stroke-width="5" role="img" aria-label="Photo of a house front with red projected hearts and purple porch lighting"/>
  </svg>

  <section class="events-panel">
    <h2 class="events-title">PERFECT<br>FOR SPECIAL<br>EVENTS</h2>
    <ul class="events-list">
      <li>Parties</li>
      <li>Graduation</li>
      <li>Holidays</li>
      <li>Weddings</li>
      <li>Business<br>Promotions</li>
      <li>Anytime<br>you want to<br>celebrate</li>
    </ul>
  </section>

  <p class="intro">Illuminate a projected light design and 2 colored wall washers on the exterior or interior of your home business or special event.</p>

  <section class="design-box">
    <p>Choose from many stock designs or customize<br>the image to make the design truly your own.</p>
    <div class="gobo-row">
      <svg width="440" height="76" viewBox="0 0 440 76" style="position:absolute;left:0;top:0">
        <circle cx="62" cy="38" r="35" fill="#0c0c0c" role="img" aria-label="Clover pattern design disc"/>
        <circle cx="209" cy="38" r="35" fill="#0c0c0c" role="img" aria-label="Dotted circles pattern design disc"/>
        <circle cx="288" cy="38" r="35" fill="#0c0c0c" role="img" aria-label="Tennis player silhouette design disc"/>
        <circle cx="371" cy="38" r="35" fill="#1c2a4a" stroke="#3a4d78" stroke-width="3" role="img" aria-label="Custom winter scene image disc"/>
      </svg>
      <div class="gobo-letters">ABCD<br>EFGHIJ<br>KLMNOPQ<br>RSTUV<br>WXYZ</div>
    </div>
  </section>

  <section class="offer">
    <p class="offer-lead">Rent it today for as low as</p>
    <p class="offer-price">$399</p>
    <p class="offer-term">FOR A ONE NIGHT RENTAL</p>
    <p class="offer-detail">INCLUDING ILLUMINATOR, 2 WALL WASHER,<br>INSTALLATION AND REMOVAL</p>
  </section>

  <div class="brand">
    <span class="brand-mark"></span>
    <span class="brand-name">LUMENPOINT EVENTS</span>
  </div>

  <footer class="contact-band">
    CONTACT DETAILS HERE<span class="sep"></span>PHONE<span class="sep"></span>EMAIL
  </footer>
</main>
</body>
</html>
```